Web page design for a startup, no coding

Quarrynest is a Data mining startup helping companies get data from websites. We’re looking to revamp our website to make it more professional and conversation friendly.
I need a designer to design the website in PSD and Once the PSD is done, the HTML design will be awarded as a separate job. We’ll need continues improvements to the design based on the user behaviour in the site and this can be a long term work for the right designer.
Target Market(s)
Big data, Data Mining
Industry/Entity Type
Business Software
Number of Pages Required
5+ page
Requirements
Must have
- Refer to the doc
Nice to have
- Refer to the doc
Should not have
- Refer to the doc

```html
<!DOCTYPE html>
<html lang="en">
<head>
<meta charset="utf-8">
<title>Quarrynest — Turn websites into structured data feeds</title>
<link href="https://fonts.googleapis.com/css2?family=Montserrat:wght@400;600;700&family=Open+Sans:wght@400;600&display=swap" rel="stylesheet">
<style>
:root{
  --teal:#1fcca4;
  --yellow:#f7c315;
  --orange:#f5a01e;
  --ink:#2f3336;
  --muted:#8a8f93;
  --line:#e4e6e8;
  --soft:#f4f5f6;
  --white:#ffffff;
}
*{box-sizing:border-box;margin:0;padding:0}
html,body{width:1200px;height:3144px;overflow:hidden}
body{font-family:"Open Sans",Arial,sans-serif;color:var(--ink);background:var(--white);font-size:13px;line-height:1.7}
h1,h2,h3,.brand,.nav a,.btn{font-family:"Montserrat",Arial,sans-serif}
.wrap{width:1000px;margin:0 auto;position:relative}
.btn{display:inline-block;background:var(--yellow);color:var(--white);font-weight:700;font-size:11px;letter-spacing:1px;text-transform:uppercase;padding:11px 22px;border-radius:2px}

/* header */
.site-header{height:62px}
.site-header .wrap{display:flex;align-items:center;justify-content:space-between;height:62px}
.brand{display:flex;align-items:center;gap:8px;font-weight:700;font-size:20px;color:var(--ink)}
.brand-mark{width:18px;height:18px;background:var(--ink)}
.nav{display:flex;align-items:center;gap:34px}
.nav a{font-size:11px;font-weight:600;letter-spacing:1px;color:var(--ink);text-decoration:none}

/* hero */
.hero{background:var(--teal);height:380px;color:var(--white)}
.hero .wrap{display:flex;align-items:center;height:380px}
.hero-copy{width:440px}
.hero h1{font-size:25px;line-height:1.35;font-weight:700;text-transform:uppercase;margin-bottom:16px}
.hero p{font-size:12px;opacity:.9;margin-bottom:24px;width:330px}
.hero-visual{margin-left:auto;width:520px;height:320px;border-radius:6px;background:linear-gradient(135deg,#2bd6b0,#19b893)}

/* clients */
.clients{height:120px;border-bottom:1px solid var(--line)}
.clients .wrap{display:flex;justify-content:space-between;align-items:center;height:120px;padding:0 10px}
.client{font-family:"Open Sans",Arial,sans-serif;font-weight:600;font-size:20px;color:#9a9ea2}

/* testimonial */
.testimonial{background:var(--soft);height:270px}
.testimonial .wrap{padding-top:36px}
.author{display:flex;align-items:center;justify-content:center;gap:14px;margin-bottom:22px}
.avatar{width:58px;height:58px;border-radius:50%;background:linear-gradient(#b9bdc0,#8c9195)}
.author strong{display:block;font-family:"Montserrat",Arial,sans-serif;color:var(--orange);font-size:14px}
.author span{font-size:11px;color:var(--muted)}
.quote{display:flex;gap:40px;align-items:center;padding:0 80px}
.quote-badge{flex:0 0 62px;height:62px;border-radius:50%;background:var(--orange);color:var(--white);font:700 44px/70px Georgia,serif;text-align:center}
.quote p{color:var(--muted);font-size:13px}

/* section headings */
.section-title{text-align:center;font-size:22px;font-weight:700;letter-spacing:1px;text-transform:uppercase;margin-bottom:12px}
.section-sub{text-align:center;font-size:12px;color:var(--muted);width:640px;margin:0 auto}

/* offerings */
.offerings{height:868px;padding-top:78px}
.offer-grid{display:grid;grid-template-columns:1fr 1fr;column-gap:80px;row-gap:54px;margin:80px 90px 0}
.offer{display:flex;gap:26px}
.icon{flex:0 0 56px;height:56px}
.offer h3,.reason h3{font-size:13px;font-weight:700;margin-bottom:6px}
.offer h3{color:var(--orange)}
.offer p{font-size:11px;color:var(--muted)}

/* why us */
.why{background:var(--yellow);height:688px;padding-top:66px;color:var(--white)}
.why .section-sub{color:rgba(255,255,255,.85)}
.reason-grid{display:grid;grid-template-columns:1fr 1fr;column-gap:80px;row-gap:56px;margin:70px 70px 0}
.reason{display:flex;gap:20px}
.reason .icon{flex:0 0 46px;height:46px}
.reason p{font-size:11px;color:rgba(255,255,255,.9)}

/* contact */
.contact{height:494px;padding-top:68px}
.contact .section-sub{margin-bottom:4px}
.contact .hl{color:var(--orange)}
.form{margin:40px 80px 0;display:grid;grid-template-columns:1fr 1fr;gap:14px}
.field{border:1px solid var(--line);height:42px;padding:0 16px;font-size:11px;color:#b0b4b7;display:flex;align-items:center}
.field.area{grid-column:1/3;height:120px;align-items:flex-start;padding-top:12px}
.form-actions{grid-column:1/3;display:flex;align-items:center;gap:18px;margin-top:6px}
.form-actions span{font-size:11px;color:var(--muted)}

/* footer */
.site-footer{background:var(--soft);height:262px;border-top:1px solid var(--line)}
.foot-top{display:flex;padding-top:40px}
.foot-top .brand{width:170px}
.foot-col{width:150px;list-style:none;font-size:11px;color:var(--muted);line-height:2.1}
.foot-col li{text-transform:uppercase;letter-spacing:.5px}
.foot-top .btn{margin-left:auto;height:34px;padding:10px 18px}
.social{display:flex;justify-content:center;gap:12px;margin-top:34px}
.social span{width:12px;height:12px;border-radius:50%;background:#6c7074}
.copy{text-align:center;font-size:10px;color:var(--muted);margin-top:10px;letter-spacing:.5px}
</style>
</head>
<body>

<header class="site-header">
  <div class="wrap">
    <div class="brand"><span class="brand-mark"></span>Quarrynest</div>
    <nav class="nav">
      <a>SOLUTIONS</a><a>PRICING</a><a>COMPANY</a>
      <span class="btn">Request a Quote</span>
    </nav>
  </div>
</header>

<section class="hero">
  <div class="wrap">
    <div class="hero-copy">
      <h1>Turn websites into<br>structured data feeds</h1>
      <p>We crawl, clean and deliver web data so your team can focus on using it, not collecting it, with accurate feeds on a schedule.</p>
      <span class="btn">Get Started Now</span>
    </div>
    <div class="hero-visual" role="img" aria-label="Illustration of a desk seen from above with a laptop, phone, coffee cup and notebook"></div>
  </div>
</section>

<section class="clients">
  <div class="wrap">
    <span class="client">Brightcell</span>
    <span class="client">Taskline</span>
    <span class="client">Meridia</span>
    <span class="client">Vantro</span>
    <span class="client">Startloop</span>
    <span class="client">Nicheway</span>
  </div>
</section>

<section class="testimonial">
  <div class="wrap">
    <div class="author">
      <div class="avatar" role="img" aria-label="Portrait photo of the customer"></div>
      <div><strong>Rohan Mathew</strong><span>at Brightcell</span></div>
    </div>
    <div class="quote">
      <div class="quote-badge">“</div>
      <p>We used to spend weeks collecting product details by hand. Since moving to Quarrynest our catalogue is refreshed every night and our analysts finally work on insights instead of spreadsheets. The team is responsive, the data is clean and the delivery has never missed a day for us.</p>
    </div>
  </div>
</section>

<section class="offerings">
  <h2 class="section-title">Our Offerings</h2>
  <p class="section-sub">Businesses of all sizes use our web data feeds to make faster decisions. Explore the solutions built for your industry and goals.</p>
  <div class="offer-grid">
    <div class="offer">
      <svg class="icon" viewBox="0 0 56 56" fill="none" stroke="#2f3336" stroke-width="2"><rect x="4" y="8" width="48" height="36"/><line x1="4" y1="16" x2="52" y2="16"/><line x1="12" y1="26" x2="30" y2="26"/><line x1="12" y1="34" x2="24" y2="34"/><line x1="20" y1="50" x2="36" y2="50"/></svg>
      <div><h3>E-commerce</h3><p>Track prices, stock and reviews across online stores and keep your catalogue ahead of every competitor in the market.</p></div>
    </div>
    <div class="offer">
      <svg class="icon" viewBox="0 0 56 56" fill="none" stroke="#2f3336" stroke-width="2"><path d="M6 40a22 22 0 0 1 44 0"/><line x1="28" y1="40" x2="40" y2="24"/><circle cx="28" cy="40" r="3"/><line x1="6" y1="46" x2="50" y2="46"/></svg>
      <div><h3>Lead Generation</h3><p>Build fresh prospect lists from public directories and listings, filtered by industry, region and company size.</p></div>
    </div>
    <div class="offer">
      <svg class="icon" viewBox="0 0 56 56" fill="none" stroke="#2f3336" stroke-width="2"><rect x="4" y="8" width="48" height="36"/><polyline points="12,36 22,26 30,32 44,18"/><line x1="20" y1="50" x2="36" y2="50"/></svg>
      <div><h3>SERP Tracking</h3><p>Monitor search rankings for your keywords every day and see how your pages move against rival sites.</p></div>
    </div>
    <div class="offer">
      <svg class="icon" viewBox="0 0 56 56" fill="none" stroke="#2f3336" stroke-width="2"><circle cx="18" cy="14" r="6"/><path d="M8 44V28h20v16"/><rect x="32" y="18" width="18" height="26"/><line x1="36" y1="26" x2="46" y2="26"/><line x1="36" y1="34" x2="46" y2="34"/></svg>
      <div><h3>Price Aggregation</h3><p>Combine prices from many sources into one feed for comparison tools, marketplaces and pricing teams.</p></div>
    </div>
    <div class="offer">
      <svg class="icon" viewBox="0 0 56 56" fill="none" stroke="#2f3336" stroke-width="2"><circle cx="28" cy="14" r="7"/><path d="M16 34a12 12 0 0 1 24 0"/><rect x="8" y="38" width="40" height="12"/><circle cx="12" cy="16" r="4"/><circle cx="44" cy="16" r="4"/></svg>
      <div><h3>Recruiting</h3><p>Gather job postings and candidate profiles from career sites to find talent and watch hiring trends.</p></div>
    </div>
    <div class="offer">
      <svg class="icon" viewBox="0 0 56 56" fill="none" stroke="#2f3336" stroke-width="2"><rect x="4" y="8" width="48" height="40"/><line x1="4" y1="16" x2="52" y2="16"/><polyline points="20,24 12,32 20,40"/><polyline points="36,24 44,32 36,40"/><line x1="31" y1="22" x2="25" y2="42"/></svg>
      <div><h3>Build Your App</h3><p>Power your own product with reliable data delivered through an API, ready for dashboards and apps.</p></div>
    </div>
  </div>
</section>

<section class="why">
  <h2 class="section-title">Why Us ?</h2>
  <p class="section-sub">Businesses of all sizes choose Quarrynest for accuracy, speed and support. Here is what makes our data service different.</p>
  <div class="reason-grid">
    <div class="reason">
      <svg class="icon" viewBox="0 0 46 46" fill="none" stroke="#ffffff" stroke-width="2"><rect x="4" y="8" width="38" height="28"/><line x1="15" y1="42" x2="31" y2="42"/><polyline points="14,22 20,28 32,16"/></svg>
      <div><h3>Fully Managed</h3><p>We handle setup, crawling, cleaning and quality checks end to end. You simply receive the data in the format you need, on the schedule you choose, with no servers to run.</p></div>
    </div>
    <div class="reason">
      <svg class="icon" viewBox="0 0 46 46" fill="none" stroke="#ffffff" stroke-width="2"><circle cx="23" cy="23" r="18"/><polyline points="23,12 23,23 31,28"/></svg>
      <div><h3>Always On Time</h3><p>Our platform runs around the clock and recovers from site changes fast, so your feeds arrive when promised and your reports never wait on missing data.</p></div>
    </div>
    <div class="reason">
      <svg class="icon" viewBox="0 0 46 46" fill="none" stroke="#ffffff" stroke-width="2"><path d="M23 4l16 6v12c0 10-7 17-16 20C14 39 7 32 7 22V10z"/><polyline points="16,23 21,28 30,18"/></svg>
      <div><h3>Reliable Quality</h3><p>Every dataset passes automated and manual checks for gaps and errors before delivery, giving you clean records you can trust in every decision.</p></div>
    </div>
    <div class="reason">
      <svg class="icon" viewBox="0 0 46 46" fill="none" stroke="#ffffff" stroke-width="2"><path d="M6 10h34v22H20l-8 8v-8H6z"/><line x1="13" y1="18" x2="33" y2="18"/><line x1="13" y1="24" x2="27" y2="24"/></svg>
      <div><h3>Helpful Support</h3><p>A dedicated engineer works with you from the first call, answers questions quickly and adapts the feed as your needs grow over time.</p></div>
    </div>
  </div>
</section>

<section class="contact">
  <h2 class="section-title">We're here to help!</h2>
  <p class="section-sub">Tell us about the data you need and our team will reply within one business day.</p>
  <p class="section-sub">Prefer to talk? <span class="hl">Request a call</span> and we will reach out.</p>
  <div class="form">
    <div class="field">Your Email Address</div>
    <div class="field">Your Phone Number</div>
    <div class="field area">Message</div>
    <div class="form-actions"><span class="btn">Send Message</span><span>We reply to every message quickly.</span></div>
  </div>
</section>

<footer class="site-footer">
  <div class="wrap">
    <div class="foot-top">
      <div class="brand"><span class="brand-mark"></span>Quarrynest</div>
      <ul class="foot-col"><li>Solutions</li><li>Pricing</li><li>Company</li></ul>
      <ul class="foot-col"><li>Blog</li><li>Careers</li><li>Case Studies</li><li>Faq</li></ul>
      <ul class="foot-col"><li>Startup Partner</li><li>Terms</li><li>Privacy</li></ul>
      <span class="btn">Request a Quote</span>
    </div>
    <div class="social"><span></span><span></span><span></span><span></span></div>
    <p class="copy">© 2024 QUARRYNEST. ALL RIGHTS RESERVED</p>
  </div>
</footer>

</body>
</html>
```